I need a label design to go on our jars of honey. Our company is called Marlowe Honey Co. The type of honey is called Ridgefern Gold Honey. The jars are 1kg. Attached is the label size. Left hand side needs to have nutritional info... as attached. Middle section is our company name, honey type, 1kg & Whangamata, NZ. Right hand side needs to have info as per photo (raw honey etc). I would like to upload more pictures... but I’m unsure how to do this? Thanks, Carol

Target Market(s)

Honey consumers... families

Industry/Entity Type

Food Production

Colors

Designer to choose colors to be used in the design.

Requirements
Must have
• Nutritional info as per upload
• Type of honey & company name as per upload
• 1kg
• Address
Nice to have
• Similar fonts to upload.
• Possibly background image... floral or beach... very faint though.

```html
<!DOCTYPE html>
<html lang="en">
<head>
<meta charset="utf-8">
<title>Marlowe Honey Co. – Ridgefern Gold Honey Label</title>
<link href="https://fonts.googleapis.com/css2?family=Amatic+SC:wght@400;700&family=Dancing+Script:wght@500&family=Satisfy&display=swap" rel="stylesheet">
<style>
  :root {
    --backdrop: #ececec;
    --label-pink: #c8679a;
    --label-pink-light: #e87fb3;
    --label-pink-deep: #ac5680;
    --ink-berry: #861a4e;
    --ink-blush: #f8e4ee;
    --rule-blush: rgba(248, 228, 238, 0.55);
    --floral-rose: #e9a6c7;
    --floral-cream: #f8e3d6;
  }
  html, body {
    margin: 0;
    padding: 0;
    width: 1200px;
    height: 918px;
    overflow: hidden;
    background: var(--backdrop);
  }
  .label {
    position: absolute;
    left: 60px;
    top: 190px;
    width: 1080px;
    height: 540px;
  }
  .label-shape {
    position: absolute;
    inset: 0;
  }
  .floral-crown {
    position: absolute;
    left: 385px;
    top: 22px;
    width: 310px;
    height: 90px;
    border-radius: 50%;
    background: radial-gradient(ellipse at 50% 50%, var(--floral-cream) 0%, var(--floral-rose) 55%, rgba(233, 166, 199, 0) 100%);
  }

  /* Front panel */
  .front-panel {
    position: absolute;
    left: 320px;
    top: 0;
    width: 440px;
    height: 540px;
    text-align: center;
  }
  .company-name {
    position: absolute;
    left: 0;
    right: 0;
    top: 146px;
    margin: 0;
    font-family: "Amatic SC", sans-serif;
    font-weight: 400;
    font-size: 44px;
    line-height: 50px;
    letter-spacing: 0.42em;
    padding-left: 0.42em;
    color: var(--ink-blush);
  }
  .honey-type {
    position: absolute;
    left: 0;
    right: 0;
    top: 262px;
    margin: 0;
    font-family: "Satisfy", "Dancing Script", cursive;
    font-weight: 400;
    font-size: 78px;
    line-height: 86px;
    color: var(--ink-berry);
  }
  .net-weight,
  .origin {
    position: absolute;
    left: 0;
    right: 0;
    margin: 0;
    font-family: "Amatic SC", sans-serif;
    font-weight: 700;
    font-size: 20px;
    letter-spacing: 0.06em;
    color: var(--ink-blush);
  }
  .net-weight { top: 450px; }
  .origin { top: 478px; }

  /* Side panels */
  .side-panel {
    position: absolute;
    top: 150px;
    width: 260px;
    font-family: "Amatic SC", sans-serif;
    font-weight: 700;
    color: var(--ink-blush);
  }
  .nutrition-panel { left: 30px; }
  .care-panel { left: 790px; text-align: center; }
  .panel-heading {
    margin: 0 0 8px;
    font-size: 30px;
    line-height: 34px;
    letter-spacing: 0.08em;
    text-align: center;
  }
  .serving-line {
    margin: 0;
    font-size: 18px;
    line-height: 22px;
  }
  .nutrition-table {
    width: 100%;
    margin-top: 10px;
    border-collapse: collapse;
    font-size: 18px;
    line-height: 22px;
  }
  .nutrition-table th,
  .nutrition-table td {
    padding: 3px 0;
    border-bottom: 1px solid var(--rule-blush);
    text-align: right;
    font-weight: 700;
  }
  .nutrition-table th:first-child,
  .nutrition-table td:first-child { text-align: left; }
  .nutrition-table thead th { border-bottom: 2px solid var(--ink-blush); }
  .claim-list {
    list-style: none;
    margin: 0 0 18px;
    padding: 0;
    font-size: 26px;
    line-height: 36px;
    letter-spacing: 0.06em;
  }
  .care-note {
    margin: 0 0 10px;
    font-size: 19px;
    line-height: 23px;
  }
</style>
</head>
<body>
  <div class="label">
    <svg class="label-shape" width="1080" height="540" viewBox="0 0 1080 540" aria-hidden="true">
      <path d="M320 120 H330 Q350 120 365 92 Q410 6 540 4 Q670 6 715 92 Q730 120 750 120 H760 V540 H320 Z" fill="var(--label-pink)"/>
      <rect x="0" y="120" width="320" height="420" fill="var(--label-pink-light)"/>
      <rect x="760" y="120" width="320" height="420" fill="var(--label-pink-deep)"/>
    </svg>
    <div class="floral-crown" role="img" aria-label="Watercolour floral garland of pink and cream blossoms with green leaves"></div>

    <section class="side-panel nutrition-panel">
      <h2 class="panel-heading">Nutrition Information</h2>
      <p class="serving-line">Servings per pack: 50</p>
      <p class="serving-line">Serving size: 20g</p>
      <table class="nutrition-table">
        <thead>
          <tr><th></th><th>Per serve</th><th>Per 100g</th></tr>
        </thead>
        <tbody>
          <tr><td>Energy</td><td>280kJ</td><td>1400kJ</td></tr>
          <tr><td>Protein</td><td>0.1g</td><td>0.4g</td></tr>
          <tr><td>Fat total</td><td>0g</td><td>0g</td></tr>
          <tr><td>Carbohydrate</td><td>16.4g</td><td>82.1g</td></tr>
          <tr><td>Sugars</td><td>16.2g</td><td>81g</td></tr>
          <tr><td>Sodium</td><td>2mg</td><td>8mg</td></tr>
        </tbody>
      </table>
    </section>

    <div class="front-panel">
      <p class="company-name">Marlowe<br>Honey Co.</p>
      <h1 class="honey-type">Ridgefern<br>Gold Honey</h1>
      <p class="net-weight">1KG</p>
      <p class="origin">KERERU BAY N.Z.</p>
    </div>

    <section class="side-panel care-panel">
      <ul class="claim-list">
        <li>Raw Honey</li>
        <li>Unpasteurised</li>
        <li>Cold Extracted</li>
        <li>No Additives</li>
      </ul>
      <p class="care-note">Honey may crystallise naturally. Warm gently to soften.</p>
      <p class="care-note">Not suitable for infants under 12 months.</p>
      <p class="care-note">Store below 25°C.</p>
    </section>
  </div>
</body>
</html>
```